Ranked amongst the Best Colleges and Programs

the size of the ad is Full Page, with bleed*
8”x 10.75" plus 0.25" bleed'
you have two choices for the tagline .. please chose what ever you think will allow you to make a better ad.
The instructions on the brief are in red
I am looking for a hight quality modern ad to place in local weekly publications that will stand out .
I would like a ad that people will look at and say i would like to see what this ad is all about.
I apprecate creative work.
the ad should not be very crowded and the text should be able to be read.
if you decide to use people in the ad .. (you don't have to ) then it should be a male dressed in white shirt in and sports jacket.. or if you would like you can use a vector and then use male or female people.
please leave one inch on the bottom for the footer

Target Market(s)

potential middle class students from 23-35 years of age

Industry/Entity Type

education

Requirements
Must have
• .the " 98% employment rate" should stand out in the ad.. but should not be the main part of the ad
Nice to have
• creative
Should not have
• Should not be a very busy or crowded ad.. i prefer pictures of men but should be .. in a business suit .. that looks professional- white shirt

```html
<!DOCTYPE html>
<html lang="en">
<head>
<meta charset="utf-8">
<title>HCU Masters of Accounting Ad</title>
<link rel="stylesheet" href="https://fonts.googleapis.com/css2?family=Barlow:wght@400;500;700;800&display=swap">
<style>
  :root {
    --page-bg: #eceef0;
    --paper: #ffffff;
    --blue-pale: #d6e3ec;
    --blue-mid: #87abc5;
    --blue-head: #6b8fad;
    --ink: #111111;
    --body-ink: #222222;
    --photo-light: #e8f0f6;
    --photo-dark: #8fa9bf;
  }
  * { margin: 0; padding: 0; box-sizing: border-box; }
  html, body {
    width: 1200px; height: 1200px; overflow: hidden;
    background: var(--page-bg);
    font-family: "Barlow", Arial, sans-serif;
  }
  .ad {
    position: absolute; left: 200px; top: 67px;
    width: 800px; height: 1066px;
    background: var(--paper);
    overflow: hidden;
  }
  .ad-shapes, .ad-photo { position: absolute; left: 0; top: 0; width: 800px; height: 1066px; }
  .intro {
    position: absolute; left: 62px; top: 264px;
    font-size: 26px; line-height: 35px; font-weight: 500; color: var(--ink);
  }
  .program-title {
    position: absolute; left: 62px; top: 382px;
    font-size: 43px; line-height: 54px; font-weight: 800;
    color: var(--blue-head); text-transform: uppercase; letter-spacing: 0.3px;
  }
  .rankings { position: absolute; left: 62px; top: 612px; color: var(--paper); }
  .rankings-label { font-size: 28px; font-weight: 700; line-height: 36px; }
  .rankings-item { font-size: 24px; font-weight: 400; line-height: 33px; margin-top: 4px; }
  .stat { position: absolute; left: 480px; top: 596px; }
  .stat-value {
    font-size: 124px; font-weight: 800; line-height: 108px; color: var(--blue-mid);
    letter-spacing: 1px;
  }
  .stat-label {
    font-size: 38px; font-weight: 700; line-height: 46px; color: var(--ink);
    text-transform: uppercase; margin-top: 2px;
  }
  .outcomes {
    position: absolute; left: 62px; top: 840px; width: 680px;
    font-size: 21.5px; line-height: 31px; color: var(--body-ink);
  }
</style>
</head>
<body>
<main class="ad">
  <svg class="ad-shapes" viewBox="0 0 640 853" aria-hidden="true">
    <polygon class="corner-panel" points="0,0 85,0 123,73 62,196 0,196" fill="var(--blue-pale)"/>
    <polygon class="top-tab" points="125,0 315,0 292,40 145,40" fill="var(--blue-mid)"/>
    <g class="growth-arrow" stroke="var(--blue-mid)" stroke-width="3.2" fill="none">
      <polyline points="630,445 367,445 296,325"/>
    </g>
    <polygon points="288,312 312,330 292,342" fill="var(--blue-mid)"/>
    <g class="ranking-band">
      <polygon points="0,453 330,453 370,549 330,645 0,645" fill="var(--blue-mid)" opacity="0.15"/>
      <polygon points="0,453 322,453 362,549 322,645 0,645" fill="var(--paper)"/>
      <polygon points="0,453 316,453 356,549 316,645 0,645" fill="var(--blue-mid)" opacity="0.3"/>
      <polygon points="0,453 308,453 348,549 308,645 0,645" fill="var(--paper)"/>
      <polygon points="0,453 302,453 342,549 302,645 0,645" fill="var(--blue-mid)" opacity="0.5"/>
      <polygon points="0,453 296,453 336,549 296,645 0,645" fill="var(--paper)"/>
      <polygon points="0,453 290,453 330,549 290,645 0,645" fill="var(--blue-mid)"/>
    </g>
  </svg>
  <svg class="ad-photo" viewBox="0 0 640 853" role="img" aria-label="Photo of hands using a calculator and pen over financial reports">
    <defs>
      <linearGradient id="photoTone" x1="0" y1="0" x2="1" y2="1">
        <stop offset="0" stop-color="var(--photo-dark)"/>
        <stop offset="0.5" stop-color="var(--photo-light)"/>
        <stop offset="1" stop-color="#c9d6e0"/>
      </linearGradient>
    </defs>
    <polygon points="320,0 640,0 640,403 365,403 255,173" fill="url(#photoTone)"/>
  </svg>

  <p class="intro">Get ahead faster in<br>your career with a<br>prestigious HCU-</p>
  <h1 class="program-title">Masters of<br>Accounting<br>Degree</h1>

  <section class="rankings">
    <p class="rankings-label">RANKED AMONGST:</p>
    <p class="rankings-item">Best Colleges-Northgate 2023</p>
    <p class="rankings-item">Best Masters in Accounting<br>Degree - Edumeridian 2023</p>
  </section>

  <section class="stat">
    <p class="stat-value">98%</p>
    <p class="stat-label">Employment<br>Rate</p>
  </section>

  <p class="outcomes">HCS graduates have gone on to work in various high-quality jobs in top firms, earning impressive six-figure salaries as well as opening successful businesses.</p>
</main>
</body>
</html>
```